Torvane Interiors L.L.C

i need a brochure for y interior design company based in abu dhabi. the company was established in 2007 and is one of leading interior designing companies in Abu Dhabi. the company does variety of services starting from residential interior design, construction, furniture manufacturing and everything related to interior design from A-Z.
all our designs are made by our sister company ZELPHOR which is located at the same company but i do not wish to mention that in this brochure since i have a different brochure for zelphor. all pictures needed for the brochure can be taken from zelphor website (without the logo of course).

i want brief introduction about the company in the first page, and the team of work:

Torvane Interiors LLC was established in 2007 with a sole aim to cater to the interior design needs of the burgeoning housing industry and commercial advancement in the UAE.

We are an Abu Dhabi-based firm with a reputation for design excellence and budgetary responsibility. We were founded on the principle that a multi-disciplinary organization could respond with one clear vision to achieve clients' need for both functional efficiency and design excellence

Our Team

Today, our in-house team of architects, interior designers, engineers, and administrative teams continue to respond to each new challenge with technological expertise and innovative enthusiasm. The success of this approach is illustrated by the fact that more than 80 percent of our work is derived from satisfied repeat clients.

Torvane Interiors is distinguished by its diversity, simplicity, elegance and affordability. Our portfolio of projects demonstrates a variety of responses, all linked by a continuing commitment to inspire our clients and to exceed their expectations.

second page could be our services:
Our Services

We offer a wide range of services from planning, design consultancy, carpentry, furniture design and delivery of high end interiors. We mix textures, colors, ergonomics, experience and emotions. We strategize with the client to effectively blend lasting impact with bottom line budgets. We combine our client's tested values, culture and vision with our experience to create fresh, innovative and inspired spaces. We always stand out with our unique deigns by ZELPHOR and our furnishing textile by Weaver Quill.

3rd page
Residential:
(you could put few pictures of before and after or i can email some to you)

4th page:
commercial

5th page:
Retail

last page is contact page
Updates

what i want is an elegant glossy gold and black Multi purpose brochure which can be used as a blank brochure or as an A4 folder to submit quotations and other documents. so basically first page should have a photo of my own choice, but also if you open the folder in an A3 position it will have a full image of the image on the front page (so its basically half front half back kind of image).

on the inside, we will have a folded gold section down (to place a paper) on both sides right and left. on the left side, i want the Company's bio and the team.

on the right side is a glimpse of the projects (residential, commercial and retail)

all content can be taken from the website of zelphor and Lucien Marte Dubrais 

the last page (the back cover) should have our contact details which i will be posting shortly.

front image can be taken from the website of  Marte Dubrais  and if its not a good idea to put half front half back photo we can always put a full pic in the front and the same faded photo on the back.

the two pages inside could have a watermark of the logo in black on the entirely gold gloss paper with black font.

contact details are as the following:

Office #615
Noorwal Tower, Qasimat Street
Abu Dhabi
United Arab Emirates

Tel: +971-2-5550173
fax: +971-2-5550174
email: general enquiries: info@torvane-example.com
design: design@torvane-example.com
management: joulen@torvane-example.com
website: www.torvane-example.com

Industry/Entity Type

Residential

Font styles to use
Script

Colors
fee18a

Requirements
Must have
• full metalic gold with black imposing writing utside and full black inside

```html
<!DOCTYPE html>
<html lang="en">
<head>
<meta charset="utf-8">
<title>Torvane Interiors – Brochure Inside Spread</title>
<link href="https://fonts.googleapis.com/css2?family=Archivo+Narrow:wght@600;700&family=Arvo:wght@400;700&family=Great+Vibes&family=Questrial&display=swap" rel="stylesheet">
<style>
  :root {
    --page: #ffffff;
    --ink: #0b0b0b;
    --panel-dark: #121212;
    --gold: #f3c300;
    --gold-soft: #fee18a;
    --text-light: #f4f4f4;
    --label: #333333;
    --card: #2a2a2a;
  }
  * { box-sizing: border-box; margin: 0; padding: 0; }
  html, body { width: 1200px; height: 567px; overflow: hidden; background: var(--page); }
  .canvas { position: relative; width: 1200px; height: 567px; }

  .panel-label {
    position: absolute; top: 29px; width: 339px; text-align: center;
    font-family: "Arvo", serif; font-size: 18px; color: var(--label);
  }

  .spread {
    position: absolute; left: 92px; top: 69px; width: 1017px; height: 483px;
    background: var(--ink); overflow: hidden;
  }
  .panel { position: absolute; top: 0; width: 339px; height: 483px; overflow: hidden; }
  .panel--front { left: 0; background: var(--ink); }
  .panel--back { left: 339px; background: var(--panel-dark); }
  .panel--right { left: 678px; background: var(--ink); }

  .heading {
    position: absolute; display: flex; align-items: center; gap: 7px;
    font-family: "Arvo", serif; font-weight: 700; font-size: 17px; color: var(--gold);
    white-space: nowrap;
  }
  .heading svg { width: 11px; height: 12px; fill: var(--gold); }

  .body-copy {
    position: absolute; font-family: "Archivo Narrow", sans-serif; font-weight: 700;
    font-size: 10px; line-height: 15px; color: var(--text-light);
  }

  .photo { position: absolute; }

  /* front */
  .intro-heading { left: 25px; top: 22px; }
  .intro-copy { left: 25px; top: 46px; width: 300px; }
  .bedroom-photo {
    left: 0; top: 137px; width: 339px; height: 144px;
    background: linear-gradient(100deg, #8e8472 0%, #d8d3c6 30%, #ece8de 55%, #b7ad98 80%, #6f6a5e 100%);
  }
  .services-heading { left: 25px; top: 288px; }
  .services-copy { left: 25px; top: 311px; width: 300px; }

  /* back */
  .office-photo {
    left: 124px; top: 0; width: 215px; height: 119px;
    background: linear-gradient(90deg, #3a2a1e 0%, #7b5a3d 35%, #c9b7a0 70%, #8c7258 100%);
  }
  .team-heading { left: 12px; top: 101px; }
  .stripe { position: absolute; top: 130px; height: 149px; width: 6px; background: var(--gold); }
  .team-card { position: absolute; top: 134px; width: 100px; height: 145px; background: var(--card); }
  .team-card .portrait {
    position: absolute; left: 4px; top: 4px; width: 92px; height: 117px;
    background: linear-gradient(180deg, #9a9a9a 0%, #5e5e5e 100%);
  }
  .team-card .caption {
    position: absolute; left: 0; right: 0; top: 124px; text-align: center;
    font-family: "Archivo Narrow", sans-serif; font-weight: 700; font-size: 6.4px; line-height: 8px;
    color: var(--gold-soft);
  }
  .team-copy { left: 22px; top: 288px; width: 300px; line-height: 14.2px; }
  .team-copy p + p { margin-top: 7px; }
  .contact-block {
    position: absolute; left: 0; bottom: 0; width: 339px; height: 80px;
    background: linear-gradient(180deg, #1c1a10 0%, #3d3512 60%, #4a3f14 100%);
  }
  .contact-copy {
    position: absolute; left: 20px; right: 20px; top: 410px; text-align: center;
    font-family: "Archivo Narrow", sans-serif; font-weight: 700; font-size: 9.6px; line-height: 14px;
    color: var(--gold);
  }

  /* right */
  .lounge-photo {
    left: 0; top: 0; width: 339px; height: 119px;
    background: linear-gradient(90deg, #b9ac98 0%, #e7e1d5 40%, #d4c9b6 65%, #5a4330 100%);
  }
  .tagline-band { position: absolute; left: 0; top: 130px; width: 339px; height: 149px; background: var(--gold); }
  .tagline {
    position: absolute; left: 0; width: 270px; text-align: center;
    font-family: "Questrial", sans-serif; color: var(--ink); line-height: 1;
  }
  .tagline--lead { top: 12px; font-size: 17px; }
  .tagline--big { top: 31px; font-size: 21px; }
  .tagline--tail { top: 54px; font-size: 17px; }
  .tagline--small { left: 62px; width: auto; top: 79px; font-size: 10.5px; text-align: left; }
  .tagline-script {
    position: absolute; left: 82px; top: 100px; font-family: "Great Vibes", cursive;
    font-size: 38px; color: var(--ink); line-height: 1;
  }
  .project-photo { top: 291px; height: 140px; }
  .project-photo--retail { left: 8px; width: 102px; background: linear-gradient(160deg, #6a2a4f 0%, #d9c4cf 50%, #4a3b2f 100%); }
  .project-photo--dining { left: 119px; width: 100px; background: linear-gradient(160deg, #b58aa8 0%, #3b2e34 55%, #cfc2b4 100%); }
  .project-photo--hall { left: 227px; width: 102px; background: linear-gradient(160deg, #e5d7be 0%, #a08462 55%, #5a4634 100%); }
</style>
</head>
<body>
<div class="canvas">
  <div class="panel-label" style="left:92px;">Front inside</div>
  <div class="panel-label" style="left:431px;">Back inside</div>
  <div class="panel-label" style="left:770px;">Panel inside</div>

  <div class="spread">
    <!-- Front inside -->
    <section class="panel panel--front">
      <h2 class="heading intro-heading"><svg viewBox="0 0 12 13"><polygon points="0,0 12,6.5 0,13"/></svg>Intoduction</h2>
      <div class="body-copy intro-copy">Torvane Interiors LLC was established in 2007 with a sole aim to cater to the interior design needs of the burgeoning housing industry and commercial advancement in the UAE. We are an Abu Dhabi-based firm with a reputation for design excellence and budgetary responsibility.</div>
      <div class="photo bedroom-photo" role="img" aria-label="Photo of an elegant white classic bedroom with chandelier and drapes"></div>
      <h2 class="heading services-heading"><svg viewBox="0 0 12 13"><polygon points="0,0 12,6.5 0,13"/></svg>Our Services</h2>
      <div class="body-copy services-copy">We offer a wide range of services from planning, design consultancy, carpentry, furniture design and delivery of high end interiors. We mix textures, colors, ergonomics, experience and emotions. We strategize with the client to effectively blend lasting impact with bottom line budgets. We combine our client's tested values, culture and vision with our experience to create fresh, innovative and inspired spaces.</div>
    </section>

    <!-- Back inside -->
    <section class="panel panel--back">
      <div class="photo office-photo" role="img" aria-label="Photo of a wooden study with shelving and desk"></div>
      <h2 class="heading team-heading"><svg viewBox="0 0 12 13"><polygon points="0,0 12,6.5 0,13"/></svg>Our Team</h2>
      <div class="stripe" style="left:3px;"></div>
      <div class="stripe" style="left:16px;"></div>
      <div class="stripe" style="left:28px;"></div>
      <div class="team-card" style="left:50px;">
        <div class="portrait" role="img" aria-label="Portrait photo of team member Nadia Farouk"></div>
        <div class="caption">Nadia Farouk<br>Sr. Interior Design Engineer</div>
      </div>
      <div class="team-card" style="left:182px;">
        <div class="portrait" role="img" aria-label="Portrait photo of team member Ilse Varden"></div>
        <div class="caption">Ilse Varden<br>Sr. Designer</div>
      </div>
      <div class="stripe" style="left:290px;"></div>
      <div class="stripe" style="left:302px;"></div>
      <div class="stripe" style="left:314px;"></div>
      <div class="body-copy team-copy">
        <p>Today, our in-house team of architects, interior designers, engineers, and administrative teams continue to respond to each new challenge with technological expertise and innovative enthusiasm. The success of this approach is illustrated by the fact that more than 80 percent of our work is derived from satisfied repeat clients.</p>
        <p>Torvane Interiors is distinguished by its diversity, simplicity, elegance and affordability.</p>
      </div>
      <div class="contact-block" role="img" aria-label="Dark gold ornamental pattern background"></div>
      <div class="contact-copy">Office #615<br>Noorwal Tower, Qasimat Street, Abu Dhabi, United Arab Emirates<br>Tel: +971-2-5550173 &nbsp;fax: +971-2-5550174</div>
    </section>

    <!-- Panel inside -->
    <section class="panel panel--right">
      <div class="photo lounge-photo" role="img" aria-label="Photo of a bright living room with shelving and lamp"></div>
      <div class="tagline-band">
        <div class="tagline tagline--lead">SOME PEOPLE</div>
        <div class="tagline tagline--big">LOOK FOR A</div>
        <div class="tagline tagline--tail">BEAUTIFUL &nbsp;PLACE</div>
        <div class="tagline tagline--small">WE MAKE A PLACE</div>
        <div class="tagline-script">Beautiful</div>
      </div>
      <div class="photo project-photo project-photo--retail" role="img" aria-label="Photo of a retail boutique interior"></div>
      <div class="photo project-photo project-photo--dining" role="img" aria-label="Photo of a commercial dining interior"></div>
      <div class="photo project-photo project-photo--hall" role="img" aria-label="Photo of a residential hallway interior"></div>
    </section>
  </div>
</div>
</body>
</html>
```